One page flyer for nonprofit focused IT company

I need a one page flyer (one side of a single 8.5x11 page) with text and graphics. The company logo is already done, and it must appear on the flyer along with other icons and graphics. The final design will be printed on heavy weight glossy paper as a handout and also distributed as a PDF.

The text is provided in an attachment, if it needs to be shortened let me know.

Industry/Entity Type

Information Technology

Requirements
Must have
• some flare (colors, icons or images)
Should not have
• While we work for nonprofits, my company is a FOR PROFIT company.

```html
<!DOCTYPE html>
<html lang="en">
<head>
<meta charset="utf-8">
<title>Harborline Systems Corporation – Nonprofit IT Services Flyer</title>
<link href="https://fonts.googleapis.com/css2?family=Montserrat:wght@600;700;800&family=Roboto:wght@400;700&display=swap" rel="stylesheet">
<style>
  :root{
    --brand-red:#8e1428;
    --brand-red-dark:#6a0e1d;
    --brand-red-light:#a8203a;
    --tab-gray:#5b5b5b;
    --tab-edge:#3c3c3c;
    --ink:#2a2a2a;
    --paper:#ffffff;
    --backdrop:#e6e6e6;
  }
  *{box-sizing:border-box;margin:0;padding:0}
  html,body{width:1200px;height:2760px;overflow:hidden;background:var(--backdrop)}
  .canvas{position:relative;width:1200px;height:2760px}
  .flyer{
    position:absolute;left:32px;top:645px;width:946px;height:1225px;
    transform:scale(1.2);transform-origin:top left;
    background:var(--paper);overflow:hidden;
    box-shadow:0 6px 24px rgba(0,0,0,.18);
    font-family:'Roboto',Arial,sans-serif;color:var(--ink);
  }
  .header{
    position:absolute;left:0;top:0;width:946px;height:200px;
    background:linear-gradient(100deg,var(--brand-red-dark) 0%,var(--brand-red) 45%,var(--brand-red-light) 100%);
  }
  .header-notch{position:absolute;left:455px;top:199px}
  .logo-box{
    position:absolute;left:0;top:20px;width:355px;height:163px;background:var(--paper);
    display:flex;align-items:center;justify-content:center;gap:12px;
  }
  .logo-mark{width:26px;height:26px;background:var(--brand-red)}
  .logo-name{font-family:'Montserrat',Arial,sans-serif;font-weight:700;font-size:22px;color:var(--brand-red);line-height:1.15}
  .title{
    position:absolute;left:360px;top:58px;width:586px;text-align:center;color:#fff;
    font-family:'Montserrat',Arial,sans-serif;font-weight:800;line-height:1;
  }
  .title .big{font-size:58px;display:block}
  .title .sub{font-size:37px;display:block;margin-top:4px}
  .body-glow{
    position:absolute;right:0;top:200px;width:420px;height:920px;
    background:radial-gradient(ellipse at 80% 20%,rgba(0,0,0,.05),rgba(0,0,0,0) 70%);
  }
  .section{position:absolute}
  .section-head{display:flex;align-items:center;gap:12px}
  .icon{flex:0 0 40px;width:40px;height:40px}
  .section-title{
    font-family:'Montserrat',Arial,sans-serif;font-weight:700;font-size:15.5px;
    color:var(--brand-red);line-height:1.15;
  }
  .section-text{font-size:15.4px;line-height:18.6px;text-align:justify;margin-top:9px}
  .section-text b{font-weight:700}
  .intro{left:59px;top:245px;width:828px}
  .intro .section-text{margin-top:8px}
  .col-left{left:59px;width:383px}
  .col-right{left:498px;width:383px}
  .footer{
    position:absolute;left:0;top:1120px;width:946px;height:105px;
    background:linear-gradient(100deg,var(--brand-red-dark),var(--brand-red) 50%,var(--brand-red-dark));
  }
  .contact-tab{position:absolute;left:268px;top:1120px}
  .contact-label{
    position:absolute;left:268px;top:1124px;width:420px;text-align:center;
    font-family:'Montserrat',Arial,sans-serif;font-weight:800;font-size:18px;color:#fff;letter-spacing:.5px;
  }
  .contact-item{
    position:absolute;top:1184px;display:flex;align-items:center;gap:8px;
    font-family:'Montserrat',Arial,sans-serif;font-weight:700;font-size:14.5px;color:#fff;
  }
</style>
</head>
<body>
<div class="canvas">
  <article class="flyer">
    <header class="header">
      <div class="logo-box">
        <span class="logo-mark"></span>
        <span class="logo-name">Harborline Systems<br>Corporation</span>
      </div>
      <h1 class="title"><span class="big">50 YEARS OF</span><span class="sub">NONPROFIT IT SERVICES</span></h1>
    </header>
    <svg class="header-notch" width="36" height="18" viewBox="0 0 36 18"><polygon points="0,0 36,0 18,18" fill="#8e1428"/></svg>
    <div class="body-glow"></div>

    <section class="section intro">
      <div class="section-head">
        <svg class="icon" viewBox="0 0 40 40"><circle cx="20" cy="20" r="18" fill="none" stroke="#8e1428" stroke-width="2"/><circle cx="20" cy="20" r="7" fill="none" stroke="#333" stroke-width="2"/><path d="M20 8v5M20 27v5M8 20h5M27 20h5" stroke="#333" stroke-width="2"/></svg>
        <h2 class="section-title">An Efficient and Elegant Approach to IT Solution Implementations</h2>
      </div>
      <p class="section-text">Harborline Systems Corporation has been supporting the Information Systems needs of nonprofits for over 50 years. We continually strive to bring the latest technologies and best practices to nonprofits to drive down the cost of IT while implementing systems that drive revenue. Our Agile approach to IT management means that we deliver working systems to every one of our clients every two weeks.</p>
    </section>

    <section class="section col-left" style="top:390px">
      <div class="section-head">
        <svg class="icon" viewBox="0 0 40 40"><circle cx="20" cy="20" r="18" fill="none" stroke="#8e1428" stroke-width="2"/><rect x="12" y="14" width="16" height="14" fill="none" stroke="#333" stroke-width="2"/><path d="M16 14v-3h8v3" fill="none" stroke="#333" stroke-width="2"/></svg>
        <h2 class="section-title">Successes 90% Reduction in Software<br>Development Costs</h2>
      </div>
      <p class="section-text">Keystone Auto Dealers Alliance needed to update their core product offering; they engaged their in-house IT department who estimated the project would take 3 years at a cost of $3,000,000. KADA decided to work with Harborline Systems Corporation instead, and the product was released to production in only 9 months at <b>one tenth of the cost</b>, only $300,000</p>
    </section>

    <section class="section col-left" style="top:597px">
      <div class="section-head">
        <svg class="icon" viewBox="0 0 40 40"><circle cx="20" cy="20" r="18" fill="none" stroke="#8e1428" stroke-width="2"/><rect x="11" y="13" width="18" height="14" fill="none" stroke="#333" stroke-width="2"/><path d="M14 18h4M14 22h4M22 18h4M22 22h4" stroke="#333" stroke-width="1.6"/></svg>
        <h2 class="section-title">10x Increase in Membership</h2>
      </div>
      <p class="section-text">Greenway Paths Trust needed to move to online membership registration and contracted with Harborline Systems Corporation to build a significant online presence and engage potential members. Through compelling online tools and mobile applications Greenway Paths has <b>increased membership 10 fold.</b></p>
    </section>

    <section class="section col-left" style="top:773px">
      <div class="section-head">
        <svg class="icon" viewBox="0 0 40 40"><circle cx="20" cy="20" r="18" fill="none" stroke="#8e1428" stroke-width="2"/><rect x="13" y="11" width="14" height="16" fill="none" stroke="#333" stroke-width="2"/><path d="M20 27v5M16 29l4 4 4-4" fill="none" stroke="#333" stroke-width="2"/></svg>
        <h2 class="section-title">20% Reduction in Overhead</h2>
      </div>
      <p class="section-text">The National Council for Civic Equity had antiquated systems and processes in place to manage over 500 chapters across the nation. Working with HSC they implemented online tools to allow communication and management between the local chapters and national headquarters. This eliminated much of the overhead of chapter management, <b>reducing HR costs by 20%.</b></p>
    </section>

    <section class="section col-left" style="top:963px">
      <div class="section-head">
        <svg class="icon" viewBox="0 0 40 40"><circle cx="20" cy="20" r="18" fill="none" stroke="#8e1428" stroke-width="2"/><rect x="11" y="12" width="18" height="16" fill="none" stroke="#333" stroke-width="2"/><path d="M11 17h18M14 21h8M14 24h6" stroke="#333" stroke-width="1.6"/></svg>
        <h2 class="section-title">Solutions Web Applications</h2>
      </div>
      <p class="section-text">With a focus on non-profit websites and web based applications, HSC helps nonprofits communicate with their members and donors while maximizing online giving and engagement.</p>
    </section>

    <section class="section col-right" style="top:390px">
      <div class="section-head">
        <svg class="icon" viewBox="0 0 40 40"><circle cx="20" cy="20" r="18" fill="none" stroke="#8e1428" stroke-width="2"/><rect x="15" y="10" width="10" height="20" rx="2" fill="none" stroke="#333" stroke-width="2"/><circle cx="20" cy="26" r="1.2" fill="#333"/></svg>
        <h2 class="section-title">Mobile Applications</h2>
      </div>
      <p class="section-text">Harborline Systems Corporation implements mobile applications for phones and tablets to provide direct communications with members and donors enabling real-time, two way interaction.</p>
    </section>

    <section class="section col-right" style="top:538px">
      <div class="section-head">
        <svg class="icon" viewBox="0 0 40 40"><circle cx="20" cy="20" r="18" fill="none" stroke="#8e1428" stroke-width="2"/><circle cx="14" cy="16" r="4" fill="none" stroke="#333" stroke-width="2"/><circle cx="26" cy="16" r="4" fill="none" stroke="#333" stroke-width="2"/><circle cx="20" cy="26" r="4" fill="none" stroke="#333" stroke-width="2"/></svg>
        <h2 class="section-title">Systems Integration</h2>
      </div>
      <p class="section-text">Every nonprofit’s IT applications are scattered and disconnected. Harborline System Corporation has decades of experience integrating these applications into a single cohesive system.</p>
    </section>

    <section class="section col-right" style="top:680px">
      <div class="section-head">
        <svg class="icon" viewBox="0 0 40 40"><circle cx="20" cy="20" r="18" fill="none" stroke="#8e1428" stroke-width="2"/><rect x="12" y="11" width="16" height="18" fill="none" stroke="#333" stroke-width="2"/><path d="M16 25v-4M20 25v-7M24 25v-5" stroke="#333" stroke-width="2"/></svg>
        <h2 class="section-title">Business Intelligence and Reporting</h2>
      </div>
      <p class="section-text">Harborline Systems Corporation can wrestle all of an organization's data into simple executive dashboards and reports.</p>
    </section>

    <section class="section col-right" style="top:812px">
      <div class="section-head">
        <svg class="icon" viewBox="0 0 40 40"><circle cx="20" cy="20" r="18" fill="none" stroke="#8e1428" stroke-width="2"/><path d="M13 24a5 5 0 0 1 1-10 6 6 0 0 1 11 1 4 4 0 0 1 1 9z" fill="none" stroke="#333" stroke-width="2"/></svg>
        <h2 class="section-title">Cloud Migration</h2>
      </div>
      <p class="section-text">Reduce IT costs by migrating to the latest cloud solutions.</p>
    </section>

    <section class="section col-right" style="top:923px">
      <div class="section-head">
        <svg class="icon" viewBox="0 0 40 40"><circle cx="20" cy="20" r="18" fill="none" stroke="#8e1428" stroke-width="2"/><ellipse cx="20" cy="13" rx="7" ry="3" fill="none" stroke="#333" stroke-width="2"/><path d="M13 13v13c0 2 14 2 14 0V13M13 19.5c0 2 14 2 14 0" fill="none" stroke="#333" stroke-width="2"/></svg>
        <h2 class="section-title">Member Donor Database</h2>
      </div>
      <p class="section-text">Harborline Systems Corporation’s FundFlow Member / Donor CRM system is fully customized for each client meeting the unique needs of your organization.</p>
    </section>

    <footer class="footer"></footer>
    <svg class="contact-tab" width="420" height="44" viewBox="0 0 420 44">
      <polygon points="0,0 420,0 378,44 42,44" fill="#3c3c3c"/>
      <polygon points="10,0 410,0 372,38 48,38" fill="#5b5b5b"/>
    </svg>
    <div class="contact-label">CONTACT US</div>

    <div class="contact-item" style="left:72px">
      <svg width="20" height="20" viewBox="0 0 20 20"><circle cx="10" cy="10" r="9" fill="none" stroke="#fff" stroke-width="1.4"/><path d="M7 5.5l2 2-1 1.5c.6 1.3 1.7 2.4 3 3l1.5-1 2 2-1.5 1.5c-3.5-.5-6.5-3.5-7-7z" fill="#fff"/></svg>
      <span>123-456-7890</span>
    </div>
    <div class="contact-item" style="left:332px">
      <svg width="20" height="20" viewBox="0 0 20 20"><circle cx="10" cy="10" r="9" fill="none" stroke="#fff" stroke-width="1.4"/><rect x="5.5" y="7" width="9" height="6.5" fill="none" stroke="#fff" stroke-width="1.3"/><path d="M5.5 7l4.5 3.5L14.5 7" fill="none" stroke="#fff" stroke-width="1.3"/></svg>
      <span>info@harborlinesystems.com</span>
    </div>
    <div class="contact-item" style="left:650px">
      <svg width="20" height="20" viewBox="0 0 20 20"><circle cx="10" cy="10" r="9" fill="none" stroke="#fff" stroke-width="1.4"/><circle cx="10" cy="10" r="5" fill="none" stroke="#fff" stroke-width="1.2"/><path d="M5 10h10M10 5c-2 3-2 7 0 10M10 5c2 3 2 7 0 10" fill="none" stroke="#fff" stroke-width="1"/></svg>
      <span>www.harborlinesystems.com</span>
    </div>
  </article>
</div>
</body>
</html>
```